Design a New Site for a very cool Watch

We have the overall design element of the website and the banners in the PSD file. We need someone to finish our design in PSD and than convert to HTML. We have included the instructions, PSD file, images and all text.

We currently use Hubspot to host and make changes to our site. The entire design aspect is complete so all we need is some minor changes and additions within the photoshop design and than the coding into HTML.

Please only sign up if you understand photoshop and HTML conversion

Here is the DropBox link to the files
https://files.quorvel-share.net/s/pm4kx82lwq7dtne/Belthor%20Site.zip
Updates

We have the basic design concept in Photoshop.  We just need someone who can complete some changes, make some additions and convert to HTML

Target Market(s)

Watch Buyers

Requirements
Must have
• Must look like a professional luxury brand

Our brand colors are very basic with Black, White and Grey can be used

```html
<!DOCTYPE html>
<html lang="en">
<head>
<meta charset="utf-8">
<title>Belthor &amp; Co. — The Orin Watch</title>
<link rel="stylesheet" href="https://fonts.googleapis.com/css2?family=Tinos&family=Gelasio:wght@400;600;700&family=Arimo&display=swap">
<style>
  :root {
    --page: #ffffff;
    --panel: #000000;
    --ink: #ffffff;
    --soft-ink: #e6e6e6;
    --gold: #e2b94a;
    --gold-glow: rgba(214, 170, 60, 0.55);
    --card-top: #f2f2f2;
    --card-mid: #a9a9a9;
    --card-low: #3a3a3a;
    --card-edge: #ffffff;
  }
  * { margin: 0; padding: 0; box-sizing: border-box; }
  html, body { width: 1200px; height: 1200px; overflow: hidden; background: var(--page); }
  .canvas { position: relative; width: 1200px; height: 1200px; background: var(--page); }
  .site {
    position: absolute; left: 0; top: 139px; width: 1162px; height: 922px;
    background: var(--panel); color: var(--ink);
  }
  .brand {
    position: absolute; left: 34px; top: 50px; width: 330px;
    font-family: "Tinos", "Times New Roman", serif;
    font-size: 34px; line-height: 40px; letter-spacing: 0.5px;
    color: var(--ink); white-space: nowrap; overflow: hidden;
  }
  .main-nav {
    position: absolute; left: 388px; top: 70px;
    display: flex; align-items: center;
    font-family: "Gelasio", Georgia, serif; font-weight: 700; font-size: 20px;
  }
  .main-nav a {
    color: var(--gold); text-decoration: none;
    background: rgba(0,0,0,0.85);
    box-shadow: 0 0 14px 4px rgba(120, 100, 60, 0.35);
    padding: 0 1px;
  }
  .main-nav .sep { color: var(--gold); margin: 0 7px; font-weight: 400; }
  .hero-image {
    position: absolute; left: 86px; top: 133px; width: 296px; height: 312px;
    background: radial-gradient(circle at 20% 45%, #c9c9c9 0%, #9a9a9a 45%, #6e6e6e 75%, #000 100%);
    border-radius: 0 50% 50% 0 / 0 50% 50% 0;
  }
  .slider-arrow { position: absolute; width: 22px; height: 40px; }
  .slider-arrow.prev { left: 36px; top: 259px; }
  .slider-arrow.next { left: 1128px; top: 262px; }
  .hero-copy {
    position: absolute; left: 420px; top: 148px; width: 660px;
    font-family: "Tinos", "Times New Roman", serif; font-size: 20px; line-height: 25px;
    color: var(--soft-ink);
  }
  .hero-copy p { margin-bottom: 25px; }
  .hero-copy .learn-more { color: var(--soft-ink); text-decoration: none; }
  .feature-cards { position: absolute; left: 0; top: 481px; width: 1162px; height: 216px; }
  .feature-card {
    position: absolute; top: 0; width: 216px; height: 216px;
    border: 2px solid var(--card-edge);
    border-radius: 6px 6px 44px 44px;
    background: linear-gradient(to bottom, var(--card-mid) 34%, #7a7a7a 65%, var(--card-low) 100%);
    box-shadow: 0 0 26px 8px var(--gold-glow);
    overflow: hidden;
  }
  .feature-card .card-strip {
    position: absolute; left: 2px; right: 2px; top: 6px; height: 70px;
    background: linear-gradient(160deg, #6d6d6d 0%, #bdbdbd 35%, var(--card-top) 100%);
  }
  .feature-card .card-label {
    position: absolute; left: 0; right: 0; top: 140px;
    text-align: center; font-family: "Gelasio", Georgia, serif; font-weight: 600;
    font-size: 19px; line-height: 22px; color: var(--gold);
  }
  .footer-links {
    position: absolute; left: 0; width: 1132px; top: 782px;
    display: flex; justify-content: center; gap: 24px;
    font-family: "Arimo", Arial, sans-serif; font-size: 16px; letter-spacing: -0.3px;
  }
  .footer-links a { color: var(--ink); text-decoration: none; }
  .copyright {
    position: absolute; left: 0; width: 1132px; top: 846px; text-align: center;
    font-family: "Arimo", Arial, sans-serif; font-size: 14px; color: var(--ink);
  }
  .copyright sup { font-size: 11px; }
</style>
</head>
<body>
<div class="canvas">
  <div class="site">
    <div class="brand">BELTHOR &amp; CO.</div>

    <nav class="main-nav">
      <a href="#">Home</a><span class="sep">|</span>
      <a href="#">About Us</a><span class="sep">|</span>
      <a href="#">Contact</a><span class="sep">|</span>
      <a href="#">Colletion</a><span class="sep">|</span>
      <a href="#">Lifestyle</a><span class="sep">|</span>
      <a href="#">Media</a><span class="sep">|</span>
      <a href="#">Shop Now</a>
    </nav>

    <svg class="slider-arrow prev" viewBox="0 0 22 40" aria-label="Previous slide"><polygon points="22,0 22,40 0,20" fill="#ffffff"/></svg>
    <div class="hero-image" role="img" aria-label="Photograph of the moon's surface"></div>
    <div class="hero-copy">
      <p>How did we put the Universe in the Orin Watch</p>
      <p>Over the years……..</p>
      <p>A small amount of fragments from the&nbsp; Moon, Mars and other rare celes-<br>tial treasures from the universe have fallen to Earth.</p>
      <p><a class="learn-more" href="#">LEARN MORE</a></p>
    </div>
    <svg class="slider-arrow next" viewBox="0 0 22 40" aria-label="Next slide"><polygon points="0,0 0,40 22,20" fill="#ffffff"/></svg>

    <div class="feature-cards">
      <a class="feature-card" style="left:0px" href="#">
        <div class="card-strip" role="img" aria-label="Brushed metal plate with embossed brand name"></div>
        <div class="card-label">The Orin Story</div>
      </a>
      <a class="feature-card" style="left:235px" href="#">
        <div class="card-strip" role="img" aria-label="Brushed metal plate with embossed brand name"></div>
        <div class="card-label">Register Your Watch</div>
      </a>
      <a class="feature-card" style="left:470px" href="#">
        <div class="card-strip" role="img" aria-label="Brushed metal plate with embossed brand name"></div>
        <div class="card-label">Repair,Maintenance<br>&amp; Warranty Info</div>
      </a>
      <a class="feature-card" style="left:706px" href="#">
        <div class="card-strip" role="img" aria-label="Brushed metal plate with embossed brand name"></div>
        <div class="card-label">Register to find out<br>about new watch<br>collection</div>
      </a>
      <a class="feature-card" style="left:941px" href="#">
        <div class="card-strip" role="img" aria-label="Brushed metal plate with embossed brand name"></div>
        <div class="card-label">Spread the World</div>
      </a>
    </div>

    <div class="footer-links">
      <a href="#">CONTACT US</a>
      <a href="#">TERMS OF SERVICE</a>
      <a href="#">REFUND POLICY</a>
      <a href="#">PRIVACY POLICY</a>
    </div>
    <div class="copyright">Copyright(C) by Belthor &amp; Co <sup>TM</sup>. All rights reserved.</div>
  </div>
</div>
</body>
</html>
```